Quillbrook Builders Business Cards

I want to use the logo and make an unique business card that shows the textured Logo with brick and builings. I want to be able to stand out when I pass out business cards.

```html
<!DOCTYPE html>
<html lang="en">
<head>
<meta charset="utf-8">
<title>Quillbrook Builders Business Cards</title>
<link href="https://fonts.googleapis.com/css2?family=Lato:wght@400;700;900&display=swap" rel="stylesheet">
<style>
  :root {
    --stage: #1b1b1b;
    --card: #000000;
    --accent: #e0491f;
    --ink-light: #ffffff;
  }
  * { box-sizing: border-box; margin: 0; padding: 0; }
  html, body { width: 900px; height: 1200px; overflow: hidden; }
  body {
    background: var(--stage);
    font-family: 'Lato', sans-serif;
    position: relative;
  }
  .card {
    position: absolute;
    left: 123px;
    width: 655px;
    height: 374px;
    border-radius: 22px;
    background: var(--card);
    overflow: hidden;
  }
  .card-front { top: 206px; }
  .card-back { top: 621px; }

  .brand {
    position: absolute;
    display: flex;
    flex-direction: column;
    align-items: center;
    justify-content: center;
    gap: 14px;
    color: var(--ink-light);
    font-weight: 900;
    text-align: center;
    text-transform: uppercase;
  }
  .brand-mark {
    width: 26px;
    height: 26px;
    background: var(--accent);
  }
  .card-front .brand {
    left: 179px; top: 62px; width: 300px; height: 250px;
    font-size: 34px; line-height: 1.05; letter-spacing: 1px;
  }
  .card-back .brand {
    left: 320px; top: 84px; width: 300px; height: 244px;
    font-size: 34px; line-height: 1.05; letter-spacing: 1px;
  }
  .card-back .brand-mark { background: var(--card); border: 2px solid var(--ink-light); }

  .accent-band {
    position: absolute;
    left: 0; right: 0; top: 205px; bottom: 0;
    background: var(--accent);
  }
  .name-bar {
    position: absolute;
    left: 0; top: 56px;
    width: 6px; height: 45px;
    background: var(--accent);
  }
  .holder-name {
    position: absolute;
    left: 28px; top: 50px;
    font-size: 25px; font-weight: 700;
    color: var(--accent);
  }
  .holder-role {
    position: absolute;
    left: 28px; top: 84px;
    font-size: 17px;
    color: var(--ink-light);
  }
  .address {
    position: absolute;
    left: 32px; top: 216px;
    font-size: 17px; line-height: 22px;
    color: var(--ink-light);
  }
  .contact-list {
    position: absolute;
    left: 31px; top: 276px;
    list-style: none;
    color: var(--ink-light);
    font-size: 17px;
  }
  .contact-list li {
    display: flex; align-items: center; gap: 10px;
    height: 26.5px;
  }
  .contact-list svg { width: 17px; height: 17px; flex: none; }
</style>
</head>
<body>
  <section class="card card-front">
    <div class="brand">
      <span class="brand-mark"></span>
      <span>Quillbrook<br>Builders</span>
    </div>
  </section>

  <section class="card card-back">
    <div class="accent-band"></div>
    <span class="name-bar"></span>
    <h1 class="holder-name">Jonathan Smith</h1>
    <p class="holder-role">Owner</p>
    <p class="address">421, Address line goes here<br>45452, Country name</p>
    <ul class="contact-list">
      <li>
        <svg viewBox="0 0 24 24" fill="#fff" aria-hidden="true"><path d="M6.6 10.8a15.1 15.1 0 0 0 6.6 6.6l2.2-2.2c.3-.3.7-.4 1-.2 1.1.4 2.3.6 3.6.6.6 0 1 .4 1 1V20c0 .6-.4 1-1 1A17 17 0 0 1 3 4c0-.6.4-1 1-1h3.5c.6 0 1 .4 1 1 0 1.3.2 2.5.6 3.6.1.3 0 .7-.2 1z"/></svg>
        <span>123.456.7890</span>
      </li>
      <li>
        <svg viewBox="0 0 24 24" fill="#fff" aria-hidden="true"><path d="M2 5h20v14H2z M2 5l10 8 10-8" stroke="#e0491f" stroke-width="1.6"/></svg>
        <span>info@webname.com</span>
      </li>
      <li>
        <svg viewBox="0 0 24 24" fill="none" stroke="#fff" stroke-width="2" aria-hidden="true"><circle cx="12" cy="12" r="9.5"/><path d="M2.5 12h19M12 2.5c3 3 3 16 0 19M12 2.5c-3 3-3 16 0 19"/></svg>
        <span>www.website.com</span>
      </li>
    </ul>
    <div class="brand">
      <span class="brand-mark"></span>
      <span>Quillbrook<br>Builders</span>
    </div>
  </section>
</body>
</html>
```